Highly rated moving company needs postcard design

We need a highly converting postcard to send when people put their homes for sale online. This should highlight the fact that we're Austin's highest rated moving company, and should convey quality and value. We do local, statewide and long distance moves. We also do office and commerical moves and storage. final design must be sized to work with our mailing system. Please see attached file for more information.

```html
<!DOCTYPE html>
<html lang="en">
<head>
<meta charset="utf-8">
<title>Summit Haulers Postcard</title>
<link href="https://fonts.googleapis.com/css2?family=Montserrat:wght@400;500;600;700;800;900&display=swap" rel="stylesheet">
<style>
  :root {
    --navy: #1c1464;
    --red: #f20000;
    --red-soft: #e23a36;
    --white: #ffffff;
    --backdrop: #d2d2d2;
    --placeholder: #f2f2f2;
    --ink: #1c1464;
  }
  * { box-sizing: border-box; margin: 0; padding: 0; }
  html, body {
    width: 708px; height: 1200px; overflow: hidden;
    background: var(--backdrop);
    font-family: "Montserrat", sans-serif;
  }
  .postcard {
    position: absolute; left: 54px; width: 600px; height: 400px;
    background: var(--white); overflow: hidden;
    box-shadow: 0 6px 14px rgba(0,0,0,0.25);
  }
  .postcard--front { top: 150px; }
  .postcard--back { top: 650px; }
  .shapes { position: absolute; inset: 0; width: 600px; height: 400px; }
  .abs { position: absolute; }

  /* brand */
  .brand { display: flex; align-items: center; gap: 6px; white-space: nowrap; }
  .brand__dot { width: 30px; height: 30px; border-radius: 50%; background: var(--navy); flex: none; }
  .brand__name { font-weight: 800; color: var(--red); font-size: 16px; letter-spacing: 1px; }

  /* front */
  .truck-photo { left: 8px; top: 40px; width: 350px; height: 262px; border-radius: 6px;
    background: linear-gradient(160deg, #c9c6c4 0%, #a9a5a3 55%, #6f6a6a 100%); }
  .front-brand { left: 385px; top: 33px; }
  .kicker { left: 386px; top: 93px; font-size: 8.6px; font-weight: 800; color: var(--navy); }
  .headline { left: 384px; top: 103px; font-size: 38px; line-height: 31px; font-weight: 900; color: var(--red); }
  .lede { left: 386px; top: 173px; width: 205px; font-size: 9.3px; line-height: 11.2px; font-weight: 500; color: var(--navy); }
  .guide { color: var(--white); font-weight: 700; line-height: 1.08; }
  .guide__free { font-size: 27px; font-weight: 800; font-style: italic; display: block; }
  .guide__rest { font-size: 19px; display: block; }
  .front-guide { left: 478px; top: 232px; }
  .front-tagline { left: 46px; top: 333px; font-size: 9.4px; line-height: 11.2px; font-weight: 600; color: var(--white); }
  .contact { display: flex; align-items: center; gap: 10px; white-space: nowrap; }
  .icon { width: 20px; height: 20px; flex: none; }
  .front-phone { left: 228px; top: 331px; font-size: 17.5px; font-weight: 700; color: var(--white); }
  .front-web { left: 228px; top: 357px; font-size: 10px; font-weight: 700; color: var(--white); }

  /* back */
  .services-title { left: 25px; top: 20px; font-size: 17px; font-weight: 800; color: var(--navy); }
  .services { left: 25px; top: 49px; display: flex; gap: 9.5px; }
  .service { width: 130px; height: 171px; border: 1px solid var(--navy); padding: 6px 10px; }
  .service__photo { height: 72px; margin-bottom: 5px; }
  .service__title { font-size: 9.6px; font-weight: 700; color: var(--navy); margin-bottom: 4px; }
  .service__text { font-size: 6.4px; line-height: 7.8px; color: #2a2a3a; }
  .photo-residential { background: linear-gradient(180deg, #f4efe8, #c89c6c); }
  .photo-commercial { background: linear-gradient(180deg, #dfe7ef, #b78a5a); }
  .photo-packing { background: linear-gradient(180deg, #e8dcd2, #b98a5c); }
  .photo-piano { background: linear-gradient(180deg, #efe9e1, #b88a5b); }
  .back-guide { left: 40px; top: 269px; }
  .back-info { left: 138px; top: 265px; width: 196px; text-align: center; }
  .back-brand { justify-content: center; }
  .back-brand .brand__dot { width: 22px; height: 22px; }
  .back-brand .brand__name { font-size: 13px; }
  .back-tagline { margin-top: 8px; font-size: 9.6px; line-height: 11.2px; font-weight: 700; color: var(--navy); }
  .back-phone { left: 174px; top: 339px; font-size: 14.5px; font-weight: 700; color: var(--navy); }
  .back-web { left: 174px; top: 359px; font-size: 6.8px; font-weight: 700; color: var(--navy); }
  .back-phone .icon, .back-web .icon { width: 14px; height: 14px; }
  .back-phone.contact, .back-web.contact { gap: 12px; }
  .address-area { left: 324px; top: 232px; width: 256px; height: 154px; background: var(--placeholder); }
</style>
</head>
<body>

<section class="postcard postcard--front">
  <svg class="shapes" viewBox="0 0 600 400" aria-hidden="true">
    <polygon points="0,0 213,0 341,97 0,276" fill="var(--red-soft)"/>
    <polygon points="213,0 245,0 370,100 170,228 160,214 341,97" fill="var(--navy)"/>
    <polygon points="0,284 355,250 445,281 600,281 600,400 0,400" fill="var(--navy)"/>
    <circle cx="518" cy="282" r="69" fill="var(--navy)"/>
    <polygon points="433,330 470,320 520,316 570,320 600,326 600,400 533,400" fill="var(--red)"/>
    <polyline points="433,330 470,320 520,316 570,320 600,326" fill="none" stroke="var(--white)" stroke-width="2"/>
  </svg>

  <div class="abs truck-photo" role="img" aria-label="Photo of a white box moving truck in front of an American flag"></div>

  <div class="abs brand front-brand"><span class="brand__dot"></span><span class="brand__name">SUMMIT HAULERS</span></div>
  <p class="abs kicker">LET OUR FAMILYMOVE YOURS</p>
  <h1 class="abs headline">Austin<br>Movers</h1>
  <p class="abs lede">Austinites rave about our moving help. We’re proud to be the most dependable moving company in Austin.</p>

  <p class="abs guide front-guide"><span class="guide__free">FREE</span><span class="guide__rest">MOVING</span><span class="guide__rest">GUIDE</span></p>

  <p class="abs front-tagline">Summit Haulers is a TOP<br>rated moving company<br>from Austin, TX.</p>
  <p class="abs contact front-phone">
    <svg class="icon" viewBox="0 0 24 24" fill="none" stroke="currentColor" stroke-width="1.6"><path d="M5 3h4l2 5-3 2a12 12 0 0 0 6 6l2-3 5 2v4a2 2 0 0 1-2 2A18 18 0 0 1 3 5a2 2 0 0 1 2-2z"/></svg>
    512-555-0147</p>
  <p class="abs contact front-web">
    <svg class="icon" viewBox="0 0 24 24" fill="none" stroke="currentColor" stroke-width="1.6"><circle cx="12" cy="12" r="10"/><ellipse cx="12" cy="12" rx="4.5" ry="10"/><path d="M2 12h20M4 7h16M4 17h16"/></svg>
    www.summithaulersatx.com</p>
</section>

<section class="postcard postcard--back">
  <svg class="shapes" viewBox="0 0 600 400" aria-hidden="true">
    <circle cx="82" cy="315" r="68" fill="var(--navy)"/>
    <polygon points="0,362 40,352 90,349 140,355 164,380 150,400 0,400" fill="var(--red)"/>
    <polyline points="0,362 40,352 90,349 140,355 164,380" fill="none" stroke="var(--white)" stroke-width="2"/>
  </svg>

  <h2 class="abs services-title">Moving Services We Offer</h2>
  <div class="abs services">
    <article class="service">
      <div class="service__photo photo-residential" role="img" aria-label="Living room with sofa and stacked moving boxes"></div>
      <h3 class="service__title">Residential Moving</h3>
      <p class="service__text">We offer hassle-free residential moving services covering the Austin metropolitan area.</p>
    </article>
    <article class="service">
      <div class="service__photo photo-commercial" role="img" aria-label="Office with stacked boxes and a mover carrying a box"></div>
      <h3 class="service__title">Commercial Moving</h3>
      <p class="service__text">We offer fast and efficient commercial moving services for Austin businesses. Whether you’re moving out of a business center, a computer lab, or your law office, no office is too big or too small.</p>
    </article>
    <article class="service">
      <div class="service__photo photo-packing" role="img" aria-label="Hands taping a cardboard box"></div>
      <h3 class="service__title">Packing Services</h3>
      <p class="service__text">We offer expert packing services covering the Greater Austin area. Our skilled team can handle anything from valuable artwork to your kid’s bedroom.</p>
    </article>
    <article class="service">
      <div class="service__photo photo-piano" role="img" aria-label="Mover carrying large boxes in a bright room"></div>
      <h3 class="service__title">Piano Moving</h3>
      <p class="service__text">Needing to move a large grand piano? Our movers will move your large, heavy items quickly and professionally. We have the tools, the manpower, and the experience to get the job done right, so you can relax and leave the heavy lifting to us.</p>
    </article>
  </div>

  <p class="abs guide back-guide"><span class="guide__free">FREE</span><span class="guide__rest">MOVING</span><span class="guide__rest">GUIDE</span></p>

  <div class="abs back-info">
    <div class="brand back-brand"><span class="brand__dot"></span><span class="brand__name">SUMMIT HAULERS</span></div>
    <p class="back-tagline">Summit Haulers is a TOP<br>rated moving company<br>from Austin, TX.</p>
  </div>
  <p class="abs contact back-phone">
    <svg class="icon" viewBox="0 0 24 24" fill="none" stroke="var(--red)" stroke-width="1.8"><path d="M5 3h4l2 5-3 2a12 12 0 0 0 6 6l2-3 5 2v4a2 2 0 0 1-2 2A18 18 0 0 1 3 5a2 2 0 0 1 2-2z"/></svg>
    512-555-0147</p>
  <p class="abs contact back-web">
    <svg class="icon" viewBox="0 0 24 24" fill="none" stroke="var(--red)" stroke-width="1.8"><circle cx="12" cy="12" r="10"/><ellipse cx="12" cy="12" rx="4.5" ry="10"/><path d="M2 12h20M4 7h16M4 17h16"/></svg>
    www.summithaulersatx.com</p>

  <div class="abs address-area"></div>
</section>

</body>
</html>
```